Brill Insurance Agency - Business Cards

Hello, I am needing new trendy business cards for our Insurance Agency now that I have a new Logo. I have attached our new logo with several color options along with a business card design that I like. I am leaning towards burgundy and blue colors. I have attached our current business card. I have also attached a headshot of our company president, Martin Vale, that you can use if you wish. Thank you so much in advance for all the wonderful designs!!!!

Target Market(s)

We want to look very professional to potential customers and we also want to look very professional so insurance companies will want to contract with us to sell their product.

Industry/Entity Type

Insurance

Contact Information for Business Card

Martin Vale
mvale@brillagency.com
Business: 555-213-4087
Fax: 555-213-7751
Cell: 555-390-2618
Toll Free: 888-555-0194
42 W Elm Rd Butler, MO 64730
www.brillagency.net

Font styles to use
Serif
Sans Serif

Colors
0355a3
3277b5
f04a50
ec1f27

Requirements
Nice to have
• I love creativity. The more creative and balanced a business card design the more I will like it. I would like the card to be printed horizontally instead of vertically.
Should not have
• My project should not have the Allied Coverage Network logo. It is no longer used in the industry.

```html
<!DOCTYPE html>
<html lang="en">
<head>
<meta charset="utf-8">
<title>Brill Insurance Agency – Business Cards</title>
<link rel="stylesheet" href="https://fonts.googleapis.com/css2?family=Montserrat:wght@300;400;600;700&display=swap">
<style>
  :root {
    --backdrop: #2e2420;
    --navy: #0d3a5e;
    --burgundy: #8c1a3f;
    --teal: #1fa98e;
    --strip-blue: #0f3d68;
    --white: #ffffff;
    --ink-muted: #e9e3e6;
    --photo-light: #8a8a8e;
    --photo-dark: #1d1d22;
  }
  * { box-sizing: border-box; margin: 0; padding: 0; }
  html, body {
    width: 1200px; height: 831px; overflow: hidden;
    background: var(--backdrop);
    font-family: "Montserrat", sans-serif;
  }
  .canvas { position: relative; width: 1200px; height: 831px; }

  .card {
    position: absolute; width: 540px; height: 310px;
    overflow: hidden; border-radius: 3px;
    box-shadow: 0 10px 30px rgba(0,0,0,.45);
  }

  /* Back of card */
  .card-back { left: 40px; top: 100px; background: var(--navy); }
  .card-back .wordmark {
    position: absolute; left: 0; right: 0; top: 128px;
    display: flex; align-items: center; justify-content: center; gap: 14px;
  }
  .wordmark-dot { width: 38px; height: 38px; border-radius: 50%; background: var(--white); }
  .wordmark-name {
    color: var(--white); font-weight: 700; font-size: 22px;
    letter-spacing: .5px; text-transform: uppercase; line-height: 1;
  }

  /* Front of card */
  .card-front { left: 620px; top: 420px; background: var(--white); }
  .band-burgundy {
    position: absolute; left: 0; right: 0; top: 100px; height: 150px;
    background: var(--burgundy);
  }
  .band-divider {
    position: absolute; left: 0; right: 0; top: 250px; height: 5px; background: var(--white);
  }
  .band-blue {
    position: absolute; left: 0; right: 0; top: 255px; bottom: 0; background: var(--strip-blue);
  }
  .portrait {
    position: absolute; left: 0; top: 30px; width: 215px; height: 220px;
    background: linear-gradient(180deg, var(--photo-light) 0%, var(--photo-dark) 70%);
  }
  .front-logo {
    position: absolute; right: 26px; top: 40px;
    display: flex; align-items: center; gap: 10px;
  }
  .front-logo .wordmark-dot { width: 30px; height: 30px; background: var(--teal); }
  .front-logo .wordmark-name { color: var(--teal); font-size: 15px; }

  .contact-block { position: absolute; left: 238px; top: 114px; color: var(--white); }
  .person-name { color: var(--teal); font-weight: 700; font-size: 22px; line-height: 1.1; }
  .person-title { font-weight: 300; font-size: 15px; margin-top: 2px; margin-bottom: 10px; }
  .contact-list { list-style: none; }
  .contact-list li {
    display: flex; align-items: center; gap: 10px;
    font-size: 15px; font-weight: 400; line-height: 1.45;
  }
  .contact-list svg { width: 14px; height: 14px; flex: none; }
  .address {
    position: absolute; left: 238px; top: 268px;
    color: var(--ink-muted); font-size: 15px; font-weight: 400;
  }
</style>
</head>
<body>
<main class="canvas">

  <section class="card card-back" aria-label="Business card back">
    <div class="wordmark">
      <span class="wordmark-dot"></span>
      <span class="wordmark-name">Brill Insurance Agency Inc</span>
    </div>
  </section>

  <section class="card card-front" aria-label="Business card front">
    <div class="band-burgundy"></div>
    <div class="band-divider"></div>
    <div class="band-blue"></div>
    <div class="portrait" role="img" aria-label="Headshot of the agent in a dark suit and red tie"></div>

    <div class="front-logo">
      <span class="wordmark-dot"></span>
      <span class="wordmark-name">Brill Insurance Agency Inc</span>
    </div>

    <div class="contact-block">
      <p class="person-name">Your Name</p>
      <p class="person-title">Your Title</p>
      <ul class="contact-list">
        <li>
          <svg viewBox="0 0 24 24" aria-hidden="true"><path fill="#1fa98e" d="M6.6 10.8a15.1 15.1 0 0 0 6.6 6.6l2.2-2.2c.3-.3.7-.4 1-.2 1.1.4 2.3.6 3.6.6.6 0 1 .4 1 1V20c0 .6-.4 1-1 1A17 17 0 0 1 3 4c0-.6.4-1 1-1h3.5c.6 0 1 .4 1 1 0 1.3.2 2.5.6 3.6.1.3 0 .7-.2 1z"/></svg>
          123-456-2100
        </li>
        <li>
          <svg viewBox="0 0 24 24" aria-hidden="true"><rect x="2" y="5" width="20" height="14" rx="1" fill="#1fa98e"/><path d="M2.5 5.5 12 13l9.5-7.5" fill="none" stroke="#8c1a3f" stroke-width="1.8"/></svg>
          youremail@mailpost.com
        </li>
        <li>
          <svg viewBox="0 0 24 24" aria-hidden="true"><circle cx="12" cy="12" r="10" fill="#1fa98e"/><path d="M2 12h20M12 2c3 3 3 17 0 20M12 2c-3 3-3 17 0 20" fill="none" stroke="#8c1a3f" stroke-width="1.5"/></svg>
          www.yourwebsite.com
        </li>
      </ul>
    </div>

    <p class="address">Your address, city, state, ZIP 0000</p>
  </section>

</main>
</body>
</html>
```